12 page New Church Launch Booklet

I have a 12 page 8.5x11 Mock-up of a Launch booklet I need to get done and made ready to be sent to Pressvale.com for printing. I have uploaded the 12 pages and the content that I need. I need to have this designed from scratch while being inspired by the mock-up. I am open to new concepts and design ideas from the designer. I would like to use some of the pictures that are included in the mock-up but if there are other options that will work better i am open to that.

Target Market(s)

Churches who support church plants and individuals who may be interested in joining the launch team.

Font styles to use
Serif

Colors

Designer to choose colors to be used in the design.

Requirements
Must have
• I have uploaded a mock-up. i just want something that will be appealing to the eye.

```html
<!DOCTYPE html>
<html lang="en">
<head>
<meta charset="utf-8">
<title>Kindle Church Launch Booklet</title>
<link href="https://fonts.googleapis.com/css2?family=Lora:wght@400;600;700&display=swap" rel="stylesheet">
<style>
:root{
  --backdrop:#dcdde0;
  --ink:#0c0c0c;
  --white:#ffffff;
  --grey-text:#c4c4c4;
  --flame-top:#e8452c;
  --flame-mid:#ee6a25;
  --flame-low:#f3a01f;
}
*{box-sizing:border-box;margin:0;padding:0}
html,body{width:1200px;height:3599px;overflow:hidden}
body{background:var(--backdrop);font-family:"Lora",serif;color:var(--white)}
.sheet{height:899.75px;display:flex;align-items:center;justify-content:center}
.spread{display:flex;box-shadow:0 18px 40px rgba(0,0,0,.25)}
.single{box-shadow:0 18px 40px rgba(0,0,0,.25)}
.page{position:relative;width:450px;height:582px;background:var(--ink);overflow:hidden}
.region{position:absolute}
.wordmark{position:absolute;font-weight:600;font-size:24px;line-height:1;color:var(--white);display:flex;align-items:center;gap:10px;white-space:nowrap}
.wordmark .dot{width:12px;height:12px;border-radius:50%;background:var(--flame-mid)}

/* front cover */
.cover .flame-art{left:255px;top:60px;width:195px;height:440px;border-radius:120px 0 0 160px;background:linear-gradient(to bottom,var(--flame-top),var(--flame-mid) 50%,var(--flame-low))}
.cover .crowd{left:0;right:0;bottom:0;height:170px;background:linear-gradient(to bottom,rgba(12,12,12,0),#2a1d14 70%,#35241a)}
.launch{position:absolute;left:40px;top:270px;width:210px}
.launch .kicker{font-size:18px;letter-spacing:1px}
.launch .date{font-weight:700;font-size:22px;color:var(--flame-mid);margin-top:2px}
.launch .rule{width:70px;height:2px;background:var(--flame-mid);margin:10px 0}
.launch .tagline{font-size:16px;color:var(--grey-text);line-height:1.3}
.url{position:absolute;left:40px;bottom:30px;font-size:11px;letter-spacing:.8px;color:var(--white)}

/* back cover */
.involve{position:absolute;left:28px;top:230px;width:394px;height:82px;border-radius:10px;background:linear-gradient(90deg,var(--flame-top),var(--flame-low));display:flex;align-items:center;padding:0 16px;gap:14px;color:var(--ink)}
.involve h2{font-weight:700;font-size:12.5px;line-height:1.3;width:118px;flex:none}
.involve ul{list-style:none;border-left:1px solid var(--ink);padding-left:12px;display:grid;grid-template-columns:1fr 1fr;gap:6px 10px;font-size:10px;line-height:1.3}
.involve li::before{content:"\25CE\00a0"}
.contact{position:absolute;left:28px;top:345px;display:flex;gap:18px;align-items:flex-start}
.contact .wordmark{position:static;font-size:20px}
.contact .info{border-left:1px solid var(--grey-text);padding-left:16px}
.contact h3{font-weight:400;font-size:11px;letter-spacing:.8px;margin-bottom:8px}
.contact p{font-size:10px;margin-bottom:6px;display:flex;align-items:center;gap:8px}
.contact p i{width:10px;height:10px;border-radius:50%;background:var(--flame-mid);display:inline-block;flex:none}

/* page 1 */
.page1 .flame-art{left:0;top:50px;width:200px;height:532px;border-radius:0 140px 0 0;background:linear-gradient(to bottom,var(--flame-top),var(--flame-mid) 55%,var(--flame-low))}
.page1 .person{left:26px;top:160px;width:160px;height:422px;border-radius:80px 80px 0 0;background:linear-gradient(to bottom,#2b2b2b,#141414)}
.bio{position:absolute;left:218px;top:60px;width:206px}
.bio h1{font-weight:400;font-size:24px;line-height:1.1}
.bio h1 b{font-weight:700;color:var(--flame-top)}
.bio p{font-size:9px;line-height:1.5;margin-top:10px}
.bio h4{margin-top:20px;font-weight:600;font-size:12px;letter-spacing:.8px;color:var(--flame-mid)}
.ticks{list-style:none;margin-top:9px}
.ticks li{position:relative;padding-left:17px;font-size:9px;line-height:1.4;margin-bottom:8px}
.ticks li svg{position:absolute;left:0;top:1px;width:11px;height:11px}
.tab{position:absolute;right:0;bottom:24px;width:88px;height:30px;display:flex;align-items:center;justify-content:center;font-size:11px}
.tab.orange{background:var(--flame-low);color:var(--ink)}
.tab.dark{background:var(--ink);color:var(--white);border-top:3px solid var(--flame-low)}

/* page 2 */
.page2{background:linear-gradient(to bottom,var(--flame-top),var(--flame-mid) 55%,var(--flame-low))}
.page2 .preaching{right:0;bottom:0;width:210px;height:220px;background:linear-gradient(to bottom,rgba(243,160,31,0),rgba(190,110,30,.55))}
.page2 .couple{left:0;top:0;width:232px;height:582px;border-radius:0 44px 44px 0;border-right:5px solid var(--ink);background:linear-gradient(135deg,#cfcfcf,#6c6c6c 55%,#222)}
.community{position:absolute;left:252px;top:50px;width:176px}
.community h4{font-weight:600;font-size:13px;letter-spacing:.8px;line-height:1.2;margin-bottom:10px}
</style>
</head>
<body>

<section class="sheet">
  <div class="single">
    <article class="page cover">
      <div class="region crowd" role="img" aria-label="Dim photo of a worship crowd with raised hands"></div>
      <div class="region flame-art" role="img" aria-label="Large orange flame graphic"></div>
      <div class="wordmark" style="left:40px;top:50px"><span class="dot"></span>Kindle Church</div>
      <div class="launch">
        <div class="kicker">LAUNCHING</div>
        <div class="date">APRIL 12, 2020</div>
        <div class="rule"></div>
        <div class="tagline">A multi-ethnic church planting church</div>
      </div>
      <div class="url">www.kindlechurchhub.org</div>
    </article>
  </div>
</section>

<section class="sheet">
  <div class="spread">
    <article class="page back">
      <div class="involve">
        <h2>CONSIDER FOUR WAYS TO GET INVOLVED.</h2>
        <ul><li>Pray</li><li>Give Sacrificially</li><li>Join Launch Team</li><li>Join Behind the Scenes</li></ul>
      </div>
      <div class="contact">
        <div class="wordmark"><span class="dot"></span>Kindle Church</div>
        <div class="info">
          <h3>FOR MORE INFORMATION</h3>
          <p><i></i>info@kindlechurchhub.org</p>
          <p><i></i>555-014-2290</p>
          <p><i></i>kindlechurchhub.org</p>
        </div>
      </div>
    </article>
    <article class="page cover">
      <div class="region crowd" role="img" aria-label="Dim photo of a worship crowd with raised hands"></div>
      <div class="region flame-art" role="img" aria-label="Large orange flame graphic"></div>
      <div class="wordmark" style="left:40px;top:50px"><span class="dot"></span>Kindle Church</div>
      <div class="launch">
        <div class="kicker">LAUNCHING</div>
        <div class="date">APRIL 12, 2020</div>
        <div class="rule"></div>
        <div class="tagline">A multi-ethnic church planting church</div>
      </div>
      <div class="url">www.kindlechurchhub.org</div>
    </article>
  </div>
</section>

<section class="sheet">
  <div class="spread">
    <article class="page page1">
      <div class="region flame-art" role="img" aria-label="Orange flame graphic behind the pastor"></div>
      <div class="region person" role="img" aria-label="Photo of the lead pastor standing in a dark polo shirt"></div>
      <div class="bio">
        <h1>I am <b>MARCUS</b></h1>
        <p>Marcus Hale was born and raised as a preacher's kid in the central city. At a young age he moved into ministry, serving youth and young adults. After a season of teaching, he said yes to a call to plant a church in the heart of the city.</p>
        <p>In 2016, he led the launch of a multi-ethnic ministry initiative. He and his wife are proud parents of four and proud grandparents of two.</p>
        <h4>EDUCATION</h4>
        <ul class="ticks">
          <li><svg viewBox="0 0 14 14"><circle cx="7" cy="7" r="6" fill="none" stroke="#ee6a25"/><path d="M4 7l2 2 4-4" fill="none" stroke="#ee6a25"/></svg>B.A. in Business from Lakeshore University</li>
          <li><svg viewBox="0 0 14 14"><circle cx="7" cy="7" r="6" fill="none" stroke="#ee6a25"/><path d="M4 7l2 2 4-4" fill="none" stroke="#ee6a25"/></svg>M.A. in Christian Ministry from Northfield Theological Seminary</li>
          <li><svg viewBox="0 0 14 14"><circle cx="7" cy="7" r="6" fill="none" stroke="#ee6a25"/><path d="M4 7l2 2 4-4" fill="none" stroke="#ee6a25"/></svg>Ed.D. in Organizational Leadership from Redstone University</li>
        </ul>
      </div>
      <div class="tab orange">Page 1</div>
    </article>
    <article class="page page2">
      <div class="region preaching" role="img" aria-label="Orange-toned photo of the pastor preaching on stage"></div>
      <div class="region couple" role="img" aria-label="Black and white photo of the pastor and his wife smiling together"></div>
      <div class="community">
        <h4>COMMUNITY<br>CONNECTION</h4>
        <ul class="ticks">
          <li><svg viewBox="0 0 14 14"><circle cx="7" cy="7" r="6" fill="none" stroke="#fff"/><path d="M4 7l2 2 4-4" fill="none" stroke="#fff"/></svg>Board member of Harbor and Hands Network</li>
          <li><svg viewBox="0 0 14 14"><circle cx="7" cy="7" r="6" fill="none" stroke="#fff"/><path d="M4 7l2 2 4-4" fill="none" stroke="#fff"/></svg>Board member of Riverside High School</li>
          <li><svg viewBox="0 0 14 14"><circle cx="7" cy="7" r="6" fill="none" stroke="#fff"/><path d="M4 7l2 2 4-4" fill="none" stroke="#fff"/></svg>Member of Steering Council of Cedarline Health Care</li>
          <li><svg viewBox="0 0 14 14"><circle cx="7" cy="7" r="6" fill="none" stroke="#fff"/><path d="M4 7l2 2 4-4" fill="none" stroke="#fff"/></svg>Founder and president of Common Ground Builders, a neighborhood development organization</li>
          <li><svg viewBox="0 0 14 14"><circle cx="7" cy="7" r="6" fill="none" stroke="#fff"/><path d="M4 7l2 2 4-4" fill="none" stroke="#fff"/></svg>President of the Lakeport Declaration, a group of multi-ethnic pastors who stand as one in promoting racial unity within the body of Christ</li>
        </ul>
      </div>
      <div class="tab dark">Page 2</div>
    </article>
  </div>
</section>

<section class="sheet">
  <div class="spread">
    <article class="page page1">
      <div class="region flame-art" role="img" aria-label="Orange flame graphic behind the pastor"></div>
      <div class="region person" role="img" aria-label="Photo of the lead pastor standing in a dark polo shirt"></div>
      <div class="bio">
        <h1>I am <b>MARCUS</b></h1>
        <p>Marcus Hale was born and raised as a preacher's kid in the central city. At a young age he moved into ministry, serving youth and young adults. After a season of teaching, he said yes to a call to plant a church in the heart of the city.</p>
        <p>In 2016, he led the launch of a multi-ethnic ministry initiative. He and his wife are proud parents of four and proud grandparents of two.</p>
        <h4>EDUCATION</h4>
        <ul class="ticks">
          <li><svg viewBox="0 0 14 14"><circle cx="7" cy="7" r="6" fill="none" stroke="#ee6a25"/><path d="M4 7l2 2 4-4" fill="none" stroke="#ee6a25"/></svg>B.A. in Business from Lakeshore University</li>
          <li><svg viewBox="0 0 14 14"><circle cx="7" cy="7" r="6" fill="none" stroke="#ee6a25"/><path d="M4 7l2 2 4-4" fill="none" stroke="#ee6a25"/></svg>M.A. in Christian Ministry from Northfield Theological Seminary</li>
          <li><svg viewBox="0 0 14 14"><circle cx="7" cy="7" r="6" fill="none" stroke="#ee6a25"/><path d="M4 7l2 2 4-4" fill="none" stroke="#ee6a25"/></svg>Ed.D. in Organizational Leadership from Redstone University</li>
        </ul>
      </div>
      <div class="tab orange">Page 1</div>
    </article>
    <article class="page page2">
      <div class="region preaching" role="img" aria-label="Orange-toned photo of the pastor preaching on stage"></div>
      <div class="region couple" role="img" aria-label="Black and white photo of the pastor and his wife smiling together"></div>
      <div class="community">
        <h4>COMMUNITY<br>CONNECTION</h4>
        <ul class="ticks">
          <li><svg viewBox="0 0 14 14"><circle cx="7" cy="7" r="6" fill="none" stroke="#fff"/><path d="M4 7l2 2 4-4" fill="none" stroke="#fff"/></svg>Board member of Harbor and Hands Network</li>
          <li><svg viewBox="0 0 14 14"><circle cx="7" cy="7" r="6" fill="none" stroke="#fff"/><path d="M4 7l2 2 4-4" fill="none" stroke="#fff"/></svg>Board member of Riverside High School</li>
          <li><svg viewBox="0 0 14 14"><circle cx="7" cy="7" r="6" fill="none" stroke="#fff"/><path d="M4 7l2 2 4-4" fill="none" stroke="#fff"/></svg>Member of Steering Council of Cedarline Health Care</li>
          <li><svg viewBox="0 0 14 14"><circle cx="7" cy="7" r="6" fill="none" stroke="#fff"/><path d="M4 7l2 2 4-4" fill="none" stroke="#fff"/></svg>Founder and president of Common Ground Builders, a neighborhood development organization</li>
          <li><svg viewBox="0 0 14 14"><circle cx="7" cy="7" r="6" fill="none" stroke="#fff"/><path d="M4 7l2 2 4-4" fill="none" stroke="#fff"/></svg>President of the Lakeport Declaration, a group of multi-ethnic pastors who stand as one in promoting racial unity within the body of Christ</li>
        </ul>
      </div>
      <div class="tab dark">Page 2</div>
    </article>
  </div>
</section>

</body>
</html>
```